Harrowgate Building and Property Services needs a business card design

We need a business card design for our building and property services business. We already have a logo we just need a creative design and layout on a business card. Emphasis on clean, modern, professional.
Our client targets are mainly body corporates, building managers, construction managers.
We are a building services company that lean more to structural repair of buildings, through concrete rectification and carbon fibre strengthening.
We also refurbish facades, rendering, painting etc
We target higher end body corporates in prestigious locations, hence why we'd like our cards to reflect professionalism, strength, efficiency

Target Market(s)

body corporates, building managers, construction managers

Industry/Entity Type

Construction

Contact Information for Business Card

Harrowgate is the main word, with 'Building and Property Services' underneath.
Level 17, 88 Marsh Lane
ELMSWORTH
Melbourne
Vic 3942
T: 9218 5371
Duncan Hensley - Director
dunharrowgate@mailbox-example.net

Requirements
Must have
• Stand out on the back of the card- strong/ bold, company logo
• All of the contact details written above
Should not have
• I'd like the card to stand out, especially on the back. Id like the company logo to be prominent, although feel free to be creative around it. But remain clean and professional

```html
<!DOCTYPE html>
<html lang="en">
<head>
<meta charset="utf-8">
<title>Harrowgate Building and Property Services – Business Card</title>
<link rel="stylesheet" href="https://fonts.googleapis.com/css2?family=Cinzel:wght@400;600&family=Merriweather:wght@400&family=Roboto:wght@400&display=swap">
<style>
  :root {
    --backdrop: #4a423f;
    --card: #060709;
    --card-edge: #15171b;
    --blue: #3f9fd8;
    --blue-deep: #1a5f9a;
    --blue-soft: #7cc3ec;
    --text: #e6e8eb;
    --muted: #b9bec5;
  }
  * { margin: 0; padding: 0; box-sizing: border-box; }
  html, body { width: 1200px; height: 768px; overflow: hidden; }
  body {
    background: var(--backdrop);
    position: relative;
    font-family: "Roboto", Arial, sans-serif;
  }
  .card {
    position: absolute;
    top: 229px;
    width: 540px;
    height: 310px;
    background: var(--card);
    border: 1px solid var(--card-edge);
    border-radius: 4px;
    overflow: hidden;
    box-shadow: 0 14px 30px rgba(0,0,0,0.45);
  }
  .card-back { left: 45px; }
  .card-front { left: 615px; }

  /* back */
  .back-mark {
    position: absolute;
    inset: 0;
    display: flex;
    align-items: center;
    justify-content: center;
    gap: 14px;
  }
  .back-mark .square {
    width: 22px; height: 22px;
    border: 2px solid var(--blue-deep);
  }
  .back-mark .brand {
    font-family: "Cinzel", Georgia, serif;
    font-weight: 600;
    font-size: 34px;
    letter-spacing: 3px;
    color: var(--blue-deep);
  }

  /* front */
  .frame-lines { position: absolute; left: 0; top: 0; }
  .person {
    position: absolute;
    right: 140px;
    top: 44px;
    text-align: right;
  }
  .person-name {
    font-family: "Merriweather", Georgia, serif;
    font-size: 19px;
    color: var(--blue-soft);
    letter-spacing: 0.5px;
  }
  .person-role {
    font-size: 11px;
    color: var(--muted);
    margin-top: 3px;
  }
  .contact {
    position: absolute;
    right: 140px;
    top: 106px;
    list-style: none;
    text-align: right;
    font-size: 12.5px;
    line-height: 20px;
    color: var(--text);
  }
  .contact li { display: flex; justify-content: flex-end; align-items: center; gap: 8px; white-space: nowrap; }
  .contact .icon { width: 12px; height: 12px; flex: none; }
  .contact .spacer { width: 12px; flex: none; }

  .company {
    position: absolute;
    right: 30px;
    bottom: 30px;
    width: 220px;
    text-align: center;
  }
  .company .brand {
    font-family: "Cinzel", Georgia, serif;
    font-weight: 600;
    font-size: 24px;
    letter-spacing: 1px;
    color: var(--blue);
  }
  .company .tagline {
    font-family: "Cinzel", Georgia, serif;
    font-size: 7.5px;
    letter-spacing: 0.6px;
    color: var(--muted);
    margin-top: 2px;
  }
</style>
</head>
<body>

<section class="card card-back" aria-label="Card back">
  <div class="back-mark">
    <span class="square"></span>
    <span class="brand">HARROWGATE</span>
  </div>
</section>

<section class="card card-front" aria-label="Card front">
  <svg class="frame-lines" width="540" height="310" viewBox="0 0 540 310" aria-hidden="true">
    <defs>
      <linearGradient id="lineBlue" x1="0" y1="0" x2="1" y2="1">
        <stop offset="0" stop-color="#2f8fd0"/>
        <stop offset="0.5" stop-color="#8fd0f5"/>
        <stop offset="1" stop-color="#1b5f9c"/>
      </linearGradient>
    </defs>
    <g fill="none" stroke="url(#lineBlue)">
      <polygon points="15,15 155,155 15,295 -125,155" stroke-width="3"/>
      <polygon points="15,30 140,155 15,280 -110,155" stroke-width="1.2" opacity="0.8"/>
    </g>
  </svg>

  <div class="person">
    <div class="person-name">Duncan Hensley</div>
    <div class="person-role">Director</div>
  </div>

  <ul class="contact">
    <li>9218 5371
      <svg class="icon" viewBox="0 0 12 12" aria-hidden="true"><path d="M3 1.5 4.8 4 3.8 5.2a6 6 0 0 0 3 3L8 7.2l2.5 1.8-.8 1.8C5.5 10.8 1.2 6.5 1.2 2.3z" fill="var(--blue)"/></svg>
    </li>
    <li>dunharrowgate@mailbox-example.net
      <svg class="icon" viewBox="0 0 12 12" aria-hidden="true"><rect x="1" y="2.5" width="10" height="7" fill="var(--blue)"/><path d="M1 2.5 6 6.5 11 2.5" fill="none" stroke="#060709" stroke-width="1"/></svg>
    </li>
    <li>Level 17, 88 Marsh Lane<span class="spacer"></span></li>
    <li>ELMSWORTH Melbourne Vic 3942<span class="spacer"></span></li>
  </ul>

  <div class="company">
    <div class="brand">HARROWGATE</div>
    <div class="tagline">BUILDING AND PROPERTY SERVICES</div>
  </div>
</section>

</body>
</html>
```